Maple Row Coffee (coffee packaging design)

Project Overview:
🔥 Attention for Designer

You have been provided with detailed brand files, fonts, and reference designs for a reason. I expect work that is better than what I could create myself. The design should be thoughtful, professional, and aligned with our brand identity.

Read the full project description carefully. Every detail matters. If something is unclear, ask questions before starting. Do not just drop logos or assets onto a layout. Understand the intent and build something that fits the vision.

Rushed or mediocre work will not be accepted. I want quality over quantity with real creative thinking and brand awareness behind it.
We’re creating a high-end yet playful packaging design for Maple Row Coffee, intended to reflect the classy and nature-inspired feel of Brisk Lanes(brisklanesplaypark.example) while adding a touch of lighthearted charm.

Design Elements to Include

Logo & Brand Cues: Incorporate the Brisk Lanes logo (round circle with dog head) and use our established color palette and leafy, forestry brand patterns. This will ensure consistency and a high-end feel.

Doodle Elements (Optional): If it suits the design, feel free to incorporate the doodle-style handwriting and sketches that appear on our website (like dog names or playful notes). This adds a personal and approachable touch, though it’s not mandatory.

Bag Format: Design for a 16 oz bag, with the option to either do a full custom print or a high-quality branded sticker on a neutral bag. The goal is to make the packaging feel special and on-brand.

Overall Vibe
Think modern, classy, and a little bit whimsical. The packaging should look polished enough to be a premium product while still capturing the fun, dog-friendly personality of Brisk Lanes.
Needs: its own special logo something that can be put on cups, and stickers. We also want the bag design to feel special and not just a logo slapped onto a coffee bag, so in a way i want 2 deliverables.

fonts: in the files uploaded

Target Market(s)

Dog Owners

Font styles to use
Other font styles liked:
• Fonts are in files

Requirements
Must have
• Use our brand guidelines

```html
<!DOCTYPE html>
<html lang="en">
<head>
<meta charset="utf-8">
<title>Maple Row Coffee – 16 oz Bag Front</title>
<link rel="stylesheet" href="https://fonts.googleapis.com/css2?family=Barlow+Semi+Condensed:wght@700&family=Mali:wght@700&family=Arimo:wght@700&family=Roboto+Condensed:wght@700&display=swap">
<style>
  :root {
    --forest: #313a1b;
    --lime: #b9c022;
    --lime-soft: rgba(185, 192, 34, 0.16);
    --cream-soft: rgba(240, 214, 160, 0.13);
    --bark-soft: rgba(110, 80, 50, 0.22);
  }
  html, body {
    margin: 0;
    padding: 0;
    width: 1200px;
    height: 2349px;
    overflow: hidden;
    background: var(--forest);
  }
  .bag-front {
    position: relative;
    width: 1200px;
    height: 2349px;
    background: var(--forest);
    color: var(--lime);
    overflow: hidden;
  }
  .bag-front p,
  .bag-front h1 {
    margin: 0;
  }
  .pattern-field {
    position: absolute;
    inset: 0;
    background:
      radial-gradient(ellipse 520px 420px at 300px 260px, var(--cream-soft), transparent 70%),
      radial-gradient(ellipse 520px 420px at 900px 300px, var(--lime-soft), transparent 70%),
      radial-gradient(ellipse 300px 500px at 100px 1250px, var(--cream-soft), transparent 70%),
      radial-gradient(ellipse 300px 600px at 1080px 1300px, var(--lime-soft), transparent 70%),
      radial-gradient(ellipse 360px 420px at 130px 1800px, var(--bark-soft), transparent 70%),
      radial-gradient(ellipse 600px 380px at 350px 2200px, var(--lime-soft), transparent 70%),
      radial-gradient(ellipse 600px 380px at 900px 2150px, var(--cream-soft), transparent 70%),
      var(--forest);
  }
  .brand-dot {
    position: absolute;
    left: 486px;
    top: 596px;
    width: 228px;
    height: 228px;
    border-radius: 50%;
    background: var(--lime);
  }
  .wordmark-frame {
    position: absolute;
    left: 291px;
    top: 856px;
    width: 612px;
    height: 258px;
    border: 3px solid var(--lime);
    text-align: center;
    font-family: "Barlow Semi Condensed", sans-serif;
    font-weight: 700;
    color: var(--lime);
  }
  .wordmark-line {
    display: block;
    line-height: 1;
  }
  .wordmark-name {
    margin-top: 6px;
    font-size: 112px;
    letter-spacing: 1px;
  }
  .wordmark-coffee {
    margin-top: 0;
    font-size: 150px;
    letter-spacing: 14px;
    padding-left: 14px;
  }
  .tagline {
    position: absolute;
    top: 1322px;
    left: 0;
    width: 1200px;
    text-align: center;
    font-family: "Mali", cursive;
    font-weight: 700;
    font-size: 64px;
    line-height: 1.2;
  }
  .rule {
    position: absolute;
    left: 264px;
    width: 672px;
    height: 2px;
    background: var(--lime);
  }
  .rule-top { top: 1585px; }
  .rule-bottom { top: 1816px; }
  .promise {
    position: absolute;
    top: 1617px;
    left: 0;
    width: 1200px;
    text-align: center;
    font-family: "Arimo", sans-serif;
    font-weight: 700;
    font-size: 66px;
    line-height: 84px;
  }
  .net-weight {
    position: absolute;
    top: 1982px;
    left: 0;
    width: 1200px;
    text-align: center;
    font-family: "Roboto Condensed", sans-serif;
    font-weight: 700;
    font-size: 84px;
    line-height: 1.1;
  }
</style>
</head>
<body>
  <main class="bag-front">
    <div class="pattern-field" role="img" aria-label="Scattered pattern of small leaves, sprigs and grass doodles in lime, cream and brown"></div>

    <div class="brand-dot" aria-hidden="true"></div>

    <h1 class="wordmark-frame">
      <span class="wordmark-line wordmark-name">MAPLE ROW</span>
      <span class="wordmark-line wordmark-coffee">COFFEE</span>
    </h1>

    <p class="tagline">Crafted for Dog Lover</p>

    <div class="rule rule-top"></div>
    <p class="promise">BREWED FOR<br>DOGS BEST FRIENDS</p>
    <div class="rule rule-bottom"></div>

    <p class="net-weight">Net WT. 16 OZ</p>
  </main>
</body>
</html>
```